Finish My Wordpress Site for Local Painting Company

The site is almost done, but I'm stuck and need expert assistance. Would love to work with someone over zoom so that I can express what I've been trying to accomplish and to learn more about the back end of Wordpress. Here's what's left to be done (I think):

Upload New Photos
Gallery (Before&After)
Anchors to: Get a Quote, Gallery
Font consistency
More padding at the bottom of pages?
Edit padding on Contact page?
Links (photos, buttons, social), add domains, edit page names
Normal entrance animation?
Mobile version

And here's the site as is:
http://qv7.b19.zentrivault.example/

Coding

Coded - Design and coding required

Number of Pages Required

1 page

Colors
0355a3

Requirements
Must have
• Communication between us as the work gets done

```html
<!DOCTYPE html>
<html lang="en">
<head>
<meta charset="utf-8">
<title>Wren Hollow Painting</title>
<link rel="stylesheet" href="https://fonts.googleapis.com/css2?family=Bree+Serif&family=Signika:wght@600;700&display=swap">
<style>
:root{
  --blue:#0b5ea8;
  --blue-deep:#0355a3;
  --tan:#9b8774;
  --grey:#ababab;
  --white:#ffffff;
  --field:#f6f6f6;
  --ink:#0b5ea8;
}
*{box-sizing:border-box;margin:0;padding:0}
html,body{width:1200px;height:3681px;overflow:hidden}
body{position:relative;font-family:"Bree Serif",Georgia,serif;color:var(--white);background:var(--tan)}
.abs{position:absolute}
.center{left:0;width:1200px;text-align:center}
.hero{top:0;left:0;width:1200px;height:576px;background:linear-gradient(180deg,#3f74c4 0%,#7ea3d6 35%,#5d7d72 70%,#4a5a45 100%)}
.hero-title{top:250px;font-family:"Signika",sans-serif;font-weight:700;font-size:44px}
.hero-tag{top:306px;font-size:16px}
.nav{top:576px;left:0;width:1200px;height:84px;background:var(--blue)}
.nav-contact{left:190px;top:22px;width:230px;text-align:center;font-size:13px;line-height:24px}
.brand{left:520px;top:14px;width:160px;height:56px;display:flex;align-items:center;justify-content:center;gap:8px;font-size:13px}
.brand-dot{width:14px;height:14px;border-radius:50%;background:var(--white)}
.nav-links{left:760px;top:18px;width:240px;display:grid;grid-template-columns:repeat(3,1fr);row-gap:12px;font-size:12px;text-align:center}
.intro{top:758px;left:262px;width:676px;text-align:center;font-size:12px;line-height:23px}
.brush{width:40px;height:40px;left:580px}
.feature{width:280px;height:280px;border-radius:50%;border:3px solid #2f7fd0;top:954px;display:flex;align-items:center;justify-content:center;font-size:25px;line-height:32px;padding:0 56px}
.f1{left:143px;background:linear-gradient(135deg,#9aa0a2,#d8dcdc 50%,#6f7473)}
.f2{left:460px;background:linear-gradient(135deg,#b08a4a,#8b6a3a 50%,#5b4630)}
.f3{left:774px;background:linear-gradient(135deg,#6c9a3a,#3c6a22 55%,#a9b8c8)}
.about{top:1310px;left:250px;width:700px;text-align:center;font-size:12px;line-height:23px}
.services{top:1522px;left:0;width:1200px;height:218px;background:var(--grey)}
.svc-col{top:53px;width:300px;font-family:"Signika",sans-serif;font-weight:700;font-size:22px;line-height:37px;text-align:center}
.review{top:2362px;width:388px;height:132px;background:var(--white);border:2px solid #2f7fd0;border-radius:4px;padding:12px 14px;color:var(--ink)}
.rev-head{display:flex;align-items:center;gap:8px;font-size:13px}
.avatar{width:26px;height:26px;border-radius:50%;background:#c9cfd6}
.stars{font-size:11px;letter-spacing:1px}
.rev-text{font-size:12px;line-height:17px;margin-top:10px}
.arrow{top:2465px;font-size:20px;color:var(--white)}
.dots{top:2510px;left:535px;display:flex;gap:11px}
.dots i{width:4px;height:4px;border-radius:50%;background:#6f6050;display:block}
.dots i.on{background:#222}
.section-head{font-size:24px}
.social{display:flex;gap:6px}
.social i{width:34px;height:34px;border-radius:50%;background:var(--blue);display:block}
.signup{top:2852px;left:405px;display:flex;gap:6px}
.signup .field{width:253px;height:36px;background:var(--field);color:#8aa;font-size:12px;padding:10px 10px;border-radius:2px}
.signup .btn{width:130px;height:36px;background:var(--blue);font-size:13px;text-align:center;line-height:36px;border-radius:2px}
.quote{top:2958px;left:0;width:1200px;height:443px;background:linear-gradient(180deg,#ffffff 0%,#c9daee 35%,var(--blue) 100%)}
.quote-title{top:52px;font-family:"Signika",sans-serif;font-weight:700;font-size:38px;color:#f3f6fb}
.quote-sub{top:102px;font-size:11px;color:#b6c4d6}
.q-item{left:192px;width:340px;text-align:center;font-size:18px}
.q-form{left:608px;width:324px}
.q-field{width:324px;height:36px;background:var(--field);border:1px solid #9aa;border-radius:3px;color:#6e8aa8;font-size:11px;padding:10px 10px}
.q-send{width:324px;height:32px;background:var(--tan);border-radius:3px;text-align:center;line-height:32px;font-size:12px}
.footer{top:3401px;left:0;width:1200px;height:280px;background:var(--blue)}
.f-title{left:133px;top:52px;font-family:"Signika",sans-serif;font-weight:700;font-size:31px;line-height:34px}
.f-areas{left:133px;top:129px;width:290px;font-size:11px;line-height:23px}
.f-social{left:133px;top:203px}
.f-social i{background:var(--tan)}
.f-logo{left:556px;top:64px;width:93px;height:93px;border-radius:50%;background:var(--white);color:var(--blue);display:flex;align-items:center;justify-content:center;text-align:center;font-size:12px;line-height:15px}
.f-est{left:552px;top:183px;width:100px;text-align:center;font-size:11px}
.f-col{text-align:center;font-size:11px}
</style>
</head>
<body>

<section class="abs hero" role="img" aria-label="Photo of a restored Victorian house with a turret under a blue sky"></section>
<h1 class="abs center hero-title">Wren Hollow Painting</h1>
<p class="abs center hero-tag">Where preparation makes all the difference.</p>

<nav class="abs nav">
  <div class="abs nav-contact">(555) 014-2270<br>hello@wrenhollowpaint.example</div>
  <div class="abs brand"><span class="brand-dot"></span>Wren Hollow</div>
  <div class="abs nav-links"><span>Services</span><span>Gallery</span><span>Reviews</span><span>About</span><span>Blog</span><span>Contact</span></div>
</nav>

<p class="abs intro">At Wren Hollow's, we offer an array of paint services in the Cambridge, Waltham, and Metrowest areas. Our preparation is unparalleled, and we use nothing short of the best methods so that you can sit down and relax with a glass of lemonade, knowing that all your concerns are going to be taken care of by an expert painter you can trust.</p>

<svg class="abs brush" style="top:852px" viewBox="0 0 40 40"><path d="M36 4c-4 2-12 10-16 16l4 4c6-4 14-12 16-16z" fill="#fff"/><path d="M18 22c-6 0-10 4-10 10 0 2-2 4-4 4 6 2 14 0 16-6 1-3 0-5-2-8z" fill="#fff"/></svg>

<div class="abs feature f1" role="img" aria-label="Photo of a brush painting a white trim">Kitchen Cabinets</div>
<div class="abs feature f2" role="img" aria-label="Photo of a quote form on a clipboard">Get a Quote</div>
<div class="abs feature f3" role="img" aria-label="Photo of a paint can in front of shrubs" style="justify-content:flex-start;text-align:left;padding:0 40px 40px 56px">See what our customers have to say.</div>

<p class="abs about">We have reliable systems that help us to avoid mistakes, address every concern, and ensure your job runs seamlessly. We are lead safe certified and use environmentally friendly, zero VOC products to complete all our projects. Our crisp lines, attention to detail, personalized customer service, and competitive rates make Wren Hollow's the most unrivaled painting company you will find in the area and the best choice for all your painting needs.</p>

<svg class="abs brush" style="top:1434px" viewBox="0 0 40 40"><path d="M36 4c-4 2-12 10-16 16l4 4c6-4 14-12 16-16z" fill="#fff"/><path d="M18 22c-6 0-10 4-10 10 0 2-2 4-4 4 6 2 14 0 16-6 1-3 0-5-2-8z" fill="#fff"/></svg>

<section class="abs services">
  <div class="abs svc-col" style="left:149px">Interior<br>Pressure Wash<br>Kitchen Cabinets</div>
  <div class="abs svc-col" style="left:450px">Exterior<br>Commercial<br>Graffiti Removal</div>
  <div class="abs svc-col" style="left:750px">Carpentry<br>EMF Shielding<br>Faux &amp; Decorative</div>
</section>

<svg class="abs brush" style="top:1864px" viewBox="0 0 40 40"><path d="M36 4c-4 2-12 10-16 16l4 4c6-4 14-12 16-16z" fill="#fff"/><path d="M18 22c-6 0-10 4-10 10 0 2-2 4-4 4 6 2 14 0 16-6 1-3 0-5-2-8z" fill="#fff"/></svg>

<span class="abs arrow" style="left:186px">&lsaquo;</span>
<article class="abs review" style="left:205px">
  <div class="rev-head"><span class="avatar"></span><div>Delia R.<div class="stars">★★★★★</div></div></div>
  <p class="rev-text">When I was preparing to sell my house in Belmont, Wren Hollow did an excellent job of getting it ready in short order. The work was timely and excellent.</p>
</article>
<article class="abs review" style="left:605px">
  <div class="rev-head"><span class="avatar"></span><div>Owen T.<div class="stars">★★★★★</div></div></div>
  <p class="rev-text">Helpful, efficient, professional, fast and excellent results.</p>
</article>
<span class="abs arrow" style="left:1002px">&rsaquo;</span>
<div class="abs dots"><i></i><i class="on"></i><i></i><i></i><i></i><i></i><i></i><i></i><i></i></div>

<h2 class="abs center section-head" style="top:2592px;font-weight:400">Follow, like &amp; leave us a review.</h2>
<div class="abs social" style="top:2651px;left:502px"><i></i><i></i><i></i><i></i><i></i></div>

<svg class="abs brush" style="top:2717px" viewBox="0 0 40 40"><path d="M36 4c-4 2-12 10-16 16l4 4c6-4 14-12 16-16z" fill="#fff"/><path d="M18 22c-6 0-10 4-10 10 0 2-2 4-4 4 6 2 14 0 16-6 1-3 0-5-2-8z" fill="#fff"/></svg>

<h2 class="abs center section-head" style="top:2788px;font-weight:400">Subscribe to our newsletter.</h2>
<form class="abs signup"><div class="field">Email</div><div class="btn">Subscribe</div></form>

<section class="abs quote">
  <h2 class="abs center quote-title">Get a Quote</h2>
  <p class="abs center quote-sub">Call, email us, or just fill out the form and we'll get back to you right away.</p>
  <svg class="abs" style="left:350px;top:164px" width="26" height="26" viewBox="0 0 24 24"><path d="M20 15.5c-1.2 0-2.4-.2-3.6-.6-.3-.1-.7 0-1 .2l-2.2 2.2c-2.8-1.4-5.1-3.8-6.6-6.6l2.2-2.2c.3-.3.4-.7.2-1-.3-1.1-.5-2.3-.5-3.5 0-.6-.4-1-1-1H4c-.6 0-1 .4-1 1 0 9.4 7.6 17 17 17 .6 0 1-.4 1-1v-3.5c0-.6-.4-1-1-1z" fill="#9b8774"/></svg>
  <div class="abs q-item" style="top:207px">(555) 014-2270</div>
  <svg class="abs" style="left:349px;top:284px" width="28" height="22" viewBox="0 0 28 22"><rect width="28" height="22" rx="2" fill="#9b8774"/><path d="M2 3l12 9 12-9" stroke="#0b5ea8" stroke-width="2" fill="none"/></svg>
  <div class="abs q-item" style="top:338px">hello@wrenhollowpaint.example</div>
  <div class="abs q-form" style="top:156px"><div class="q-field">Name</div></div>
  <div class="abs q-form" style="top:204px"><div class="q-field">Email</div></div>
  <div class="abs q-form" style="top:254px"><div class="q-field" style="height:78px">Message</div></div>
  <div class="abs q-form" style="top:344px"><div class="q-send">Send</div></div>
</section>

<footer class="abs footer">
  <div class="abs f-title">Wren Hollow<br>Painting©</div>
  <p class="abs f-areas">Serving Cambridge, Waltham, Arlington, Lincoln, Belmont, Newton, Watertown, Weston, Dover, Winchester, Medford, and Lexington areas.</p>
  <div class="abs social f-social"><i></i><i></i><i></i><i></i><i></i></div>
  <div class="abs f-logo">Wren<br>Hollow</div>
  <div class="abs f-est">Est. 1985</div>

  <svg class="abs" style="left:891px;top:44px" width="26" height="26" viewBox="0 0 26 26"><circle cx="13" cy="13" r="12" fill="#9b8774"/><path d="M13 6v7l5 3" stroke="#0b5ea8" stroke-width="2.4" fill="none"/></svg>
  <div class="abs f-col" style="left:780px;top:85px;width:250px">Mon-Fri: 7am-7pm</div>
  <svg class="abs" style="left:891px;top:125px" width="24" height="24" viewBox="0 0 24 24"><path d="M20 15.5c-1.2 0-2.4-.2-3.6-.6-.3-.1-.7 0-1 .2l-2.2 2.2c-2.8-1.4-5.1-3.8-6.6-6.6l2.2-2.2c.3-.3.4-.7.2-1-.3-1.1-.5-2.3-.5-3.5 0-.6-.4-1-1-1H4c-.6 0-1 .4-1 1 0 9.4 7.6 17 17 17 .6 0 1-.4 1-1v-3.5c0-.6-.4-1-1-1z" fill="#9b8774"/></svg>
  <div class="abs f-col" style="left:780px;top:159px;width:250px">(555) 014-2270</div>
  <svg class="abs" style="left:890px;top:201px" width="26" height="20" viewBox="0 0 28 22"><rect width="28" height="22" rx="2" fill="#9b8774"/><path d="M2 3l12 9 12-9" stroke="#0b5ea8" stroke-width="2" fill="none"/></svg>
  <div class="abs f-col" style="left:730px;top:222px;width:240px">hello@wrenhollowpaint.example</div>

  <svg class="abs" style="left:1046px;top:64px" width="30" height="22" viewBox="0 0 30 22"><rect x="1" y="1" width="28" height="20" rx="2" fill="none" stroke="#9b8774" stroke-width="2"/><circle cx="9" cy="9" r="3" fill="#9b8774"/><rect x="15" y="7" width="10" height="2" fill="#9b8774"/><rect x="15" y="12" width="10" height="2" fill="#9b8774"/><rect x="5" y="14" width="8" height="3" fill="#9b8774"/></svg>
  <div class="abs f-col" style="left:940px;top:105px;width:150px;line-height:23px;text-align:right">48 Larkspur Ave, 2B<br>Cambridge, MA 02138</div>
  <div class="abs f-col" style="left:940px;top:169px;width:150px;line-height:23px;text-align:right">912 Fenwick Road, #6<br>Waltham, MA 02453</div>
</footer>

</body>
</html>
```